Valto Sàrl - Business Card

VALTO Sàrl operates in the sector Services for banks and credit institutions. It is a B2B which connects companies. The main colors should be Blue and Black. The logo and look of the card should be simple, professional, conservative and reflect Connecting People.

Target Market(s)

Financial professionals and institutions

Industry/Entity Type

Finance

Contact Information for Business Card

Chemin des Prés 9
1027 Lonay

Logo Text

Connecting dots

Font styles to use
Serif
Sans Serif

Colors
0355a3
3176b5
85acd3
cfdeed

Requirements
Should not have
• Multiple colors

```html
<!DOCTYPE html>
<html lang="en">
<head>
<meta charset="utf-8">
<title>Valto Sàrl – Business Card</title>
<link rel="stylesheet" href="https://fonts.googleapis.com/css2?family=Montserrat:wght@400;500;600;700&display=swap">
<style>
  :root {
    --blue-deep: #0355a3;
    --blue-mid: #3176b5;
    --blue-soft: #85acd3;
    --blue-pale: #cfdeed;
    --white: #ffffff;
    --paper: #f4f5f7;
    --stage: #e6e9ee;
  }
  * { box-sizing: border-box; margin: 0; padding: 0; }
  html, body { width: 1200px; height: 780px; overflow: hidden; }
  body {
    background: var(--stage);
    font-family: "Montserrat", Arial, sans-serif;
    display: flex;
    align-items: center;
    justify-content: center;
    gap: 90px;
  }
  .card {
    position: relative;
    width: 340px;
    height: 590px;
    border-radius: 18px;
    overflow: hidden;
    background: linear-gradient(180deg, var(--white), var(--paper));
    box-shadow: 0 14px 34px rgba(3, 40, 80, 0.18);
  }
  .card-art { position: absolute; inset: 0; width: 100%; height: 100%; }

  /* front */
  .brand {
    position: absolute;
    left: 0; right: 0; top: 96px;
    display: flex; align-items: center; justify-content: center; gap: 12px;
  }
  .brand-dot {
    width: 26px; height: 26px; border-radius: 50%;
    background: var(--blue-deep);
  }
  .brand-name {
    color: var(--blue-deep);
    font-weight: 600;
    font-size: 36px;
    letter-spacing: 0.5px;
  }
  .contact {
    position: absolute;
    left: 0; right: 0; top: 268px;
    text-align: center;
    color: var(--white);
  }
  .person-name {
    font-weight: 700;
    font-size: 22px;
    letter-spacing: 1px;
  }
  .person-role { font-size: 15px; font-weight: 500; margin-top: 2px; }
  .address { font-size: 14.5px; line-height: 1.4; margin-top: 14px; font-weight: 500; }
  .divider {
    display: flex; align-items: center; justify-content: center;
    gap: 10px; margin: 10px 30px 6px;
  }
  .divider::before, .divider::after {
    content: ""; flex: 1; height: 1.5px; background: var(--blue-pale); opacity: 0.85;
  }
  .icon-badge {
    width: 30px; height: 30px; border-radius: 50%;
    background: var(--white);
    display: flex; align-items: center; justify-content: center;
  }
  .icon-badge svg { width: 18px; height: 18px; }
  .contact-line { font-size: 15px; font-weight: 500; }
  .website {
    position: absolute;
    left: 0; right: 0; bottom: 30px;
    text-align: center;
    color: var(--white);
    font-size: 15px;
    font-weight: 600;
    letter-spacing: 4px;
  }

  /* back */
  .card-back .brand { top: 270px; }
  .card-back .brand-name { font-size: 40px; }
  .card-back .brand-dot { width: 30px; height: 30px; }
</style>
</head>
<body>

<section class="card card-front" aria-label="Business card front">
  <svg class="card-art" viewBox="0 0 340 590" preserveAspectRatio="none" aria-hidden="true">
    <defs>
      <linearGradient id="band-fill" x1="0" y1="0" x2="1" y2="1">
        <stop offset="0" stop-color="#0355a3"/>
        <stop offset="1" stop-color="#3176b5"/>
      </linearGradient>
    </defs>
    <path d="M0 232 Q170 200 340 262 L340 590 L0 590 Z" fill="url(#band-fill)"/>
    <path d="M40 240 Q200 218 340 270" fill="none" stroke="#cfdeed" stroke-width="2" opacity="0.8"/>
    <rect x="0" y="528" width="340" height="62" fill="#85acd3"/>
    <rect x="0" y="520" width="340" height="3" fill="#ffffff"/>
  </svg>

  <div class="brand">
    <span class="brand-dot"></span>
    <span class="brand-name">Valto Sàrl</span>
  </div>

  <div class="contact">
    <p class="person-name">LUCAS MOREL</p>
    <p class="person-role">Manager</p>
    <p class="address">Chemin des Prés 9<br>1027 Lonay</p>

    <div class="divider">
      <span class="icon-badge">
        <svg viewBox="0 0 18 18" aria-hidden="true">
          <rect x="5" y="2" width="8" height="14" rx="1.5" fill="none" stroke="#0355a3" stroke-width="1.6"/>
          <circle cx="9" cy="13.5" r="0.9" fill="#0355a3"/>
        </svg>
      </span>
    </div>
    <p class="contact-line">(021) 555 0148</p>

    <div class="divider">
      <span class="icon-badge">
        <svg viewBox="0 0 18 18" aria-hidden="true">
          <rect x="2.5" y="4.5" width="13" height="9" rx="1" fill="none" stroke="#0355a3" stroke-width="1.6"/>
          <path d="M2.8 5 L9 10 L15.2 5" fill="none" stroke="#0355a3" stroke-width="1.6"/>
        </svg>
      </span>
    </div>
    <p class="contact-line">info@valto-sarl.ch</p>
  </div>

  <p class="website">www.valto-sarl.ch</p>
</section>

<section class="card card-back" aria-label="Business card back">
  <div class="brand">
    <span class="brand-dot"></span>
    <span class="brand-name">Valto Sàrl</span>
  </div>
</section>

</body>
</html>
```